Bramwick Client Journey To Success

I need a one-page document that graphically shows the client's journey working with Bramwick from initial assessment to completed project. I want the journey to start at the "basecamp logo" and reach 4 summits (little mountain logos...) .

I'd like the imagery to convey the client starting at basecamp, and moving to each summit. Each summit, should list the subtext under each, as listed on the pdf doc i provided.

The description for the basecamp and 4 summits is attached.

I need the brochure to look like the other brochure that you did for me (attached) .

Target Market(s)

Restaurant Owners

Industry/Entity Type

Construction Management

Font styles to use
Sans Serif

Colors
EB3D1F
EC4F4E
F09395
F8D3D4
FCEDEE

Requirements
Must have
• My logo. Title: Client Journey To Success. Subtitle: The 4 Summits

```html
<!DOCTYPE html>
<html lang="en">
<head>
<meta charset="utf-8">
<title>Bramwick Development – Client Journey To Success</title>
<link rel="stylesheet" href="https://fonts.googleapis.com/css2?family=Montserrat:ital,wght@0,400;0,600;0,700;0,800;0,900;1,400;1,800;1,900&display=swap">
<style>
  :root {
    --red: #e0261e;
    --red-deep: #b81c1e;
    --red-bright: #eb3d1f;
    --ink: #111111;
    --body-text: #1a1a1a;
    --muted: #555555;
    --rule: #b5b5b5;
    --paper: #ffffff;
    --photo-dark: #3b3c3f;
    --photo-mid: #5a5c60;
  }
  * { box-sizing: border-box; margin: 0; padding: 0; }
  html, body {
    width: 972px; height: 1200px; overflow: hidden;
    background: var(--paper);
    font-family: "Montserrat", Arial, sans-serif;
  }
  .flyer { position: relative; width: 972px; height: 1200px; background: linear-gradient(180deg, #ffffff 0%, #fafafa 100%); overflow: hidden; }

  .header-art { position: absolute; left: 0; top: 0; }

  .title {
    position: absolute; right: 53px; top: 44px;
    text-align: right; color: #fff; font-weight: 900;
    font-size: 73px; line-height: 84px; letter-spacing: -1px;
    text-shadow: 3px 3px 0 rgba(0,0,0,0.55);
  }
  .subtitle {
    position: absolute; left: 520px; top: 290px; width: 220px;
    text-align: center; color: #fff; font-weight: 900; font-style: italic;
    font-size: 43px; line-height: 44px;
    text-shadow: 2px 2px 0 rgba(0,0,0,0.45);
  }

  .brand {
    position: absolute; left: 48px; top: 364px;
    display: flex; align-items: center; gap: 10px;
  }
  .brand-mark { width: 22px; height: 22px; background: var(--red); }
  .brand-name { font-weight: 800; font-size: 19px; color: var(--ink); letter-spacing: 0.2px; }

  .basecamp { position: absolute; left: 86px; top: 460px; }
  .basecamp h2 { color: var(--red); font-weight: 900; font-size: 52px; line-height: 56px; letter-spacing: -0.5px; }
  .basecamp ol { list-style: none; margin-top: 4px; }
  .basecamp li { font-weight: 800; font-size: 26px; line-height: 37px; color: var(--ink); }

  .summit { position: absolute; border-left: 3px solid var(--rule); padding-left: 18px; }
  .summit-tag { position: relative; height: 28px; }
  .summit-tag .label {
    display: inline-block; height: 28px; width: 126px;
    background: linear-gradient(90deg, var(--red-deep), var(--red-bright));
    clip-path: polygon(0 0, 80% 0, 100% 100%, 0 100%);
    color: #fff; font-weight: 700; font-size: 15px; line-height: 28px; padding-left: 12px;
  }
  .summit-tag::after {
    content: ""; position: absolute; left: 110px; right: 0; bottom: 0;
    height: 3px; background: var(--ink);
  }
  .summit h3 { font-weight: 700; font-size: 28px; line-height: 32px; color: var(--body-text); margin-top: 8px; }
  .summit ul { list-style: none; }
  .summit li { font-style: italic; font-size: 17px; line-height: 22px; color: var(--muted); letter-spacing: 0.3px; }

  .summit-1 { left: 86px; top: 676px; width: 351px; height: 210px; }
  .summit-2 { left: 542px; top: 460px; width: 354px; height: 136px; }
  .summit-3 { left: 542px; top: 617px; width: 354px; height: 157px; }
  .summit-4 { left: 542px; top: 798px; width: 354px; height: 84px; }
  .summit-3 h3 { font-size: 27px; }

  .gallery { position: absolute; top: 922px; left: 44px; display: flex; gap: 17px; }
  .gallery-photo { width: 283px; height: 162px; }
  .photo-dining { background: linear-gradient(135deg, #b92a2e 0%, #5a3a35 55%, #2e2c2e 100%); }
  .photo-windows { background: linear-gradient(135deg, #c9d6e0 0%, #e08a2e 40%, #c6621d 75%, #6e3416 100%); }
  .photo-lounge { background: linear-gradient(135deg, #e7e3de 0%, #c94a3c 45%, #7a3a2c 75%, #2f2a2a 100%); }

  .footer-band {
    position: absolute; left: 0; top: 1112px; width: 972px; height: 56px;
    background: linear-gradient(90deg, var(--red-bright) 0%, var(--red) 50%, var(--red-deep) 100%);
    color: #fff; font-weight: 700; font-size: 25px; line-height: 56px; text-align: center; letter-spacing: 0.3px;
  }
</style>
</head>
<body>
<main class="flyer">

  <svg class="header-art" width="972" height="460" viewBox="0 0 972 460" xmlns="http://www.w3.org/2000/svg">
    <defs>
      <linearGradient id="siteShade" x1="0" y1="0" x2="1" y2="1">
        <stop offset="0" stop-color="#56585c"/>
        <stop offset="0.5" stop-color="#3b3c3f"/>
        <stop offset="1" stop-color="#6a6c70"/>
      </linearGradient>
      <linearGradient id="bannerRed" x1="0" y1="0" x2="1" y2="0">
        <stop offset="0" stop-color="#c42a1f"/>
        <stop offset="0.5" stop-color="#d9352a"/>
        <stop offset="1" stop-color="#b8281e"/>
      </linearGradient>
    </defs>
    <rect class="site-photo" role="img" aria-label="Photo of construction crew in safety vests walking through a building site" x="0" y="0" width="972" height="440" fill="url(#siteShade)"/>
    <path class="brand-panel" d="M0 157 H262 Q376 157 376 271 V460 H0 Z" fill="#ffffff"/>
    <polygon class="lower-paper" points="376,384 677,438 972,312 972,460 376,460" fill="#ffffff"/>
    <polygon class="banner-shadow" points="376,372 677,428 972,302 972,313 677,440 376,385" fill="#111111"/>
    <polygon class="banner" points="376,300 972,237 972,301 677,422 376,377" fill="url(#bannerRed)"/>
  </svg>

  <h1 class="title">CLIENT JOURNEY<br>TO SUCCESS</h1>
  <p class="subtitle">THE 4<br>SUMMITS</p>

  <div class="brand">
    <span class="brand-mark"></span>
    <span class="brand-name">BRAMWICK DEVELOPMENT</span>
  </div>

  <section class="basecamp">
    <h2>BASECAMP</h2>
    <ol>
      <li>a. Client Assessment</li>
      <li>b. Determine Project Goals</li>
      <li>c. Proposal &amp; Fees</li>
    </ol>
  </section>

  <section class="summit summit-1">
    <div class="summit-tag"><span class="label">Summit 1</span></div>
    <h3>PreConstruction</h3>
    <ul>
      <li>a. Develop Project Plan</li>
      <li>b. Develop Risk Assessment &amp; Plan</li>
      <li>c. Devlelop Schedule</li>
      <li>d. Develop Budget</li>
      <li>e. Develop Team</li>
      <li>f. GC, Sub, Consultants Contracts</li>
    </ul>
  </section>

  <section class="summit summit-2">
    <div class="summit-tag"><span class="label">Summit 2</span></div>
    <h3>Execution</h3>
    <ul>
      <li>a. Acquire Permits</li>
      <li>b. PreConstruction Meeting</li>
      <li>c. Project Start</li>
    </ul>
  </section>

  <section class="summit summit-3">
    <div class="summit-tag"><span class="label">Summit 3</span></div>
    <h3>Project Management</h3>
    <ul>
      <li>a. Shared Consciousness Meetings</li>
      <li>b. Pressurized Collaboration</li>
      <li>c. Schedule Management</li>
      <li>d. Run O.O.D.A. Loop</li>
    </ul>
  </section>

  <section class="summit summit-4">
    <div class="summit-tag"><span class="label">Summit 4</span></div>
    <h3>Completion</h3>
    <ul>
      <li>a. Closeout</li>
    </ul>
  </section>

  <div class="gallery">
    <div class="gallery-photo photo-dining" role="img" aria-label="Restaurant dining room with red padded wall and rows of tables"></div>
    <div class="gallery-photo photo-windows" role="img" aria-label="Warm wood-toned dining area with angled windows and a wall sign"></div>
    <div class="gallery-photo photo-lounge" role="img" aria-label="Restaurant interior with mural wall, hanging lights and a large lit wall sign"></div>
  </div>

  <footer class="footer-band">www.bramwickbuilds.com</footer>
</main>
</body>
</html>
```